3D Buchcover für ebook
Das Design kam überraschend und war quasi aus dem Stand perfekt. Ich konnte gar nicht anders, als es zum Gewinner zu küren.
Zielgruppe
Das Buch erscheint als ebook, später auch als gedruckte Version. Es spricht Personen an, die mittels einer Diät nicht nur ihre Figur, sondern auch ihre Gesundheit, Fitneß und das Aussehen im Allgemeinen verbessern wollen. Die Hauptzielgruppe sind Frauen zwischen 35 und 60+.
Branche: Medizin/Gesundheit.
Aufgabenstellung
Hergestellt werde soll das Cover für ein ebook mit dem Titel "Der schmale Gürtel als klarer Beweis". Außerdem soll folgende Headline untegebracht werden: "Rückblick auf 13 Jahre Alltag ohne Zucker". Es soll ein Bild der Autorin verwendet werden. Aus den gelieferten Vorlagen kann die Frauenfigur ausgeschnitten werden. Wichtig ist, ihre Figur und die Ausstrahlung wirkungsvoll zur Geltung zu bringen. Unter den mitgelieferten Deteien ist außerdem das aktuelle Cover enthalten (das Buch ist bereits veröffentlicht). Auch der Autorname "Hanna Lübeck" soll auf dem Cover Platz finden.
Das Cover soll auch im Kleinformat, wie es üblicherweise in den Suchergebnissen auf Veltrix angezeigt wird, eine Aussagekraft besitzen.

```html
<!DOCTYPE html>
<html lang="de">
<head>
<meta charset="utf-8">
<title>Der schmale Gürtel als klarer Beweis – Buchcover</title>
<link rel="stylesheet" href="https://fonts.googleapis.com/css2?family=Oswald:wght@600;700&family=Open+Sans:wght@700;800&display=swap">
<style>
  :root {
    --denim-light: #aec5d9;
    --denim-mid: #86a5c2;
    --denim-dark: #5f82a4;
    --patch-navy: #142033;
    --patch-edge: #e9eef2;
    --signal-red: #e1161f;
    --signal-red-deep: #b90f17;
    --white: #ffffff;
    --ruler-light: #f4f4f2;
    --ruler-shade: #d9d9d6;
    --ink: #1d1d1f;
    --tick: #6b6b6b;
  }
  * { margin: 0; padding: 0; box-sizing: border-box; }
  html, body { width: 849px; height: 1200px; overflow: hidden; background: #ffffff; }
  .cover {
    position: relative;
    width: 849px;
    height: 1200px;
    overflow: hidden;
    font-family: "Oswald", "Arial Narrow", sans-serif;
  }
  .denim-backdrop {
    position: absolute; inset: 0;
    background: radial-gradient(ellipse at 30% 40%, var(--denim-light) 0%, var(--denim-mid) 60%, var(--denim-dark) 100%);
  }
  .torn-patch {
    position: absolute;
    left: 40px; top: 150px;
    width: 540px; height: 640px;
    background: var(--patch-navy);
    border-radius: 48% 42% 44% 50% / 40% 46% 48% 44%;
    box-shadow: 0 0 0 10px var(--patch-edge), 0 0 0 18px rgba(233,238,242,.45);
  }
  .author-photo {
    position: absolute;
    left: 565px; top: 78px;
    width: 284px; height: 1122px;
    background: linear-gradient(180deg, #c8906a 0%, #d8a88a 18%, #1d2440 28%, #161c33 100%);
    border-radius: 140px 80px 0 0;
  }
  .author-tag {
    position: absolute;
    left: 54px; top: 10px;
    width: 258px; height: 60px;
    background: var(--signal-red);
    display: flex; align-items: center; justify-content: center;
    color: var(--white);
    font-family: "Open Sans", Arial, sans-serif;
    font-weight: 700;
    font-size: 25px;
  }
  .author-tag::after {
    content: "";
    position: absolute; inset: 5px;
    border: 2px dashed rgba(255,255,255,.75);
  }
  .title {
    position: absolute; inset: 0;
    text-transform: uppercase;
    line-height: 1;
    font-weight: inherit;
  }
  .title-line { position: absolute; white-space: nowrap; }
  .title-red {
    color: var(--signal-red);
    font-weight: 700;
    -webkit-text-stroke: 3px var(--white);
    paint-order: stroke fill;
    text-shadow: 3px 3px 0 rgba(0,0,0,.25);
  }
  .title-red.first { left: 145px; top: 262px; font-size: 66px; }
  .title-red.second { left: 115px; top: 346px; font-size: 110px; }
  .title-white {
    color: var(--white);
    font-weight: 600;
    font-size: 66px;
    text-shadow: 2px 2px 0 rgba(0,0,0,.35);
  }
  .title-white.first { left: 146px; top: 499px; }
  .title-white.second { left: 204px; top: 573px; }
  .measuring-tape {
    position: absolute;
    left: 0; top: 929px;
    width: 849px; height: 111px;
    background:
      repeating-linear-gradient(90deg, var(--tick) 0 2px, transparent 2px 58px) top left / 100% 30px no-repeat,
      repeating-linear-gradient(90deg, var(--tick) 0 1px, transparent 1px 11.6px) top left / 100% 14px no-repeat,
      linear-gradient(180deg, var(--ruler-light), var(--ruler-shade));
    box-shadow: 0 4px 10px rgba(0,0,0,.3);
  }
  .tape-text {
    position: absolute;
    top: 48px;
    font-family: "Open Sans", Arial, sans-serif;
    font-weight: 800;
    font-size: 29px;
    color: var(--ink);
    white-space: nowrap;
  }
  .tape-text.lead { left: 16px; }
  .tape-text.tail { right: 16px; }
  .magnifier {
    position: absolute;
    left: 276px; top: 888px;
    width: 230px; height: 320px;
  }
  .magnifier-count {
    position: absolute;
    left: 291px; top: 930px;
    width: 158px;
    text-align: center;
    color: var(--signal-red);
    font-family: "Open Sans", Arial, sans-serif;
    font-weight: 800;
    line-height: 1;
  }
  .magnifier-count .number { display: block; font-size: 62px; }
  .magnifier-count .unit {
    display: block; font-size: 34px; margin-top: 4px;
    font-family: "Oswald", "Arial Narrow", sans-serif; font-weight: 700;
  }
</style>
</head>
<body>
<main class="cover">
  <div class="denim-backdrop" role="img" aria-label="Hellblauer Jeansstoff als Hintergrund"></div>
  <div class="torn-patch" role="img" aria-label="Ausgefranstes Loch im Jeansstoff mit dunkelblauem Stoff darunter"></div>
  <div class="author-photo" role="img" aria-label="Foto der Autorin in dunkelblauer enger Jeans und Top, sitzend, Arm auf das Knie gestützt"></div>

  <div class="author-tag">Hanna Lübeck</div>

  <h1 class="title">
    <span class="title-line title-red first">Der schmale</span>
    <span class="title-line title-red second">Gürtel</span>
    <span class="title-line title-white first">als klarer</span>
    <span class="title-line title-white second">Beweis</span>
  </h1>

  <div class="measuring-tape">
    <span class="tape-text lead">Rückblick auf</span>
    <span class="tape-text tail">Alltag ohne Zucker</span>
  </div>

  <svg class="magnifier" viewBox="0 0 230 320" aria-hidden="true">
    <line x1="150" y1="160" x2="212" y2="306" stroke="var(--signal-red-deep)" stroke-width="22" stroke-linecap="round"/>
    <line x1="150" y1="160" x2="208" y2="300" stroke="var(--signal-red)" stroke-width="14" stroke-linecap="round"/>
    <circle cx="94" cy="94" r="84" fill="var(--white)" stroke="var(--signal-red)" stroke-width="16"/>
  </svg>
  <div class="magnifier-count">
    <span class="number">13</span>
    <span class="unit">JAHRE</span>
  </div>
</main>
</body>
</html>
```